Dynamic Book Cover Design
Lines That Hold
Creative Brief
ABOUT THE PROJECT "Lines That Hold: Seven Notes from a Counselor" is a practical, warm, and deeply insightful self-help ebook written by a licensed therapist (Morgan Pellow, LPC). Unlike generic self-help books that treat boundaries like a list of aggressive demands you make on other people, this book flips the script. The core concept is that a true boundary is an internal decision about yourself. One that holds firm no matter how the other person reacts. It is about self-possession, peace, and clarity. The book will be featured on my private practice website and on Quillmart. The cover needs to instantly communicate trust, professional clinical authority, and approachable warmth. I want it to look like a book you would see prominently displayed in a high-end wellness boutique or a psychology section, rather than a loud, busy, or flashy paperback. THE DESIGN DIRECTION Style: Clean, modern, uncluttered, and grounded. Tone: Firm but kind. Calm rather than aggressive. Typography: The title needs to be highly legible and crisp, even at thumbnail size on Quillmart. Thank you so much for your time and creativity. I can't wait to see how you bring this concept to life!
Health
Adults who feel drained, over-committed, or taken advantage of, and who struggle to say no or hold a limit. Broad appeal, leaning slightly female but not exclusively. These are thoughtful readers, not looking for hype. The cover should feel calm, credible, and reassuring, like something a good therapist would hand you. But still interesting to look at.
CREATIVE FREEDOM & METAPHORS I am entirely open to your creative interpretation! If you want to use a visual metaphor for a "boundary", please do. However, I want to completely steer clear of cliché, heavy-handed imagery. Please AVOID: • Brick walls, fences, barbed wire, or stop signs. • "No" symbols or literal hands pushing someone away. • Harsh reds or alarm-style, anxiety-inducing imagery. • Cheesy, dated stock photos. • Anything that feels cold, sterile, or overly clinical. BRANDING & COLORS This book is an extension of my therapy practice, so the cover design must feel cohesive with my existing brand. Please visit my website at https://morganpellowcounsel.example to view my current color palette, aesthetic, and font family (Montserrat). I want the book to feel like it naturally belongs in that digital space. DELIVERABLES REQUIRED • Front Ebook Cover (optimized for digital/Quillmart) • Full wrap layout including a spine and back cover (for potential future print runs)

```html
<!DOCTYPE html>
<html lang="en">
<head>
<meta charset="UTF-8">
<title>Lines That Hold: Seven Notes from a Counselor</title>
<link rel="stylesheet" href="https://fonts.googleapis.com/css2?family=Oswald:wght@400;500;600&display=swap">
<style>
  :root {
    --page-bg: #e9e6e1;
    --cover-top: #f1f1f1;
    --cover-bottom: #c9c9c9;
    --ink: #2a2a2a;
    --tree-dark: #3b3a38;
    --tree-mid: #7d7b77;
    --badge-bg: #3a3a3a;
    --badge-text: #f2f2f2;
  }
  * { margin: 0; padding: 0; box-sizing: border-box; }
  html, body {
    width: 1200px;
    height: 901px;
    overflow: hidden;
    background: var(--page-bg);
  }
  .stage {
    width: 1200px;
    height: 901px;
    display: flex;
    align-items: center;
    justify-content: center;
  }
  .cover {
    position: relative;
    width: 594px;
    height: 840px;
    background: linear-gradient(180deg, var(--cover-top) 0%, #dcdcdc 55%, var(--cover-bottom) 100%);
    overflow: hidden;
    font-family: "Oswald", "Arial Narrow", sans-serif;
    color: var(--ink);
  }
  .cover-art {
    position: absolute;
    left: 0;
    top: 0;
    width: 360px;
    height: 840px;
  }
  .title-block {
    position: absolute;
    left: 270px;
    width: 300px;
    text-align: center;
    text-transform: uppercase;
  }
  .title-main {
    top: 176px;
    font-weight: 500;
    font-size: 52px;
    line-height: 1.08;
    letter-spacing: 0.5px;
  }
  .title-number {
    top: 250px;
    font-weight: 500;
    font-size: 330px;
    line-height: 1;
  }
  .title-sub {
    top: 612px;
    font-weight: 400;
    line-height: 1.05;
  }
  .title-sub .lead {
    display: block;
    font-size: 34px;
    letter-spacing: 0.5px;
  }
  .title-sub .strong {
    display: block;
    font-size: 56px;
    font-weight: 500;
    letter-spacing: 0.5px;
  }
  .author-badge {
    position: absolute;
    left: 346px;
    top: 742px;
    width: 214px;
    height: 30px;
    background: var(--badge-bg);
    color: var(--badge-text);
    font-family: "Oswald", "Arial Narrow", sans-serif;
    font-weight: 400;
    font-size: 15px;
    letter-spacing: 0.4px;
    display: flex;
    align-items: center;
    justify-content: center;
  }
</style>
</head>
<body>
  <main class="stage">
    <article class="cover">
      <svg class="cover-art" viewBox="0 0 360 840" role="img" aria-label="Photograph of a slender tree trunk and bare branches rising diagonally, with a woodpecker clinging to the bark">
        <defs>
          <linearGradient id="trunk-tone" x1="0" y1="1" x2="1" y2="0">
            <stop offset="0" stop-color="var(--tree-mid)" stop-opacity="0.55"/>
            <stop offset="0.6" stop-color="var(--tree-dark)" stop-opacity="0.45"/>
            <stop offset="1" stop-color="var(--tree-mid)" stop-opacity="0.25"/>
          </linearGradient>
        </defs>
        <rect x="0" y="0" width="360" height="840" fill="url(#trunk-tone)" opacity="0.6"/>
      </svg>

      <h1 class="title-block title-main">Lines<br>That Hold</h1>
      <div class="title-block title-number" aria-hidden="true">7</div>
      <p class="title-block title-sub">
        <span class="lead">Notes from a</span>
        <span class="strong">Counselor</span>
      </p>

      <p class="author-badge">By: Morgan Pellow, LPC</p>
    </article>
  </main>
</body>
</html>
```